Real Estate "For Sale" Sign for construction company

We need a sign that we can use to hang on a post and place on the road when we sell a property. The sign will be simple and will need to mainly feature our logo (files attached), as well as the words "For Sale", and then our phone number "(555) 617 3489". The sign will hang on a post that'll look something like the attached picture.

Target Market(s)

Home buyers

Industry/Entity Type

Real Estate

Font styles to use
Serif
Sans Serif

Colors
0054AA
0677BA
7BADD7
CADEEF
E8F1F8
0094D4
00A9DD
6FCCEA
C7EBF8
E9F6FB

Requirements
Must have
• For Sale & our phone number

```html
<!DOCTYPE html>
<html lang="en">
<head>
<meta charset="utf-8">
<title>For Sale Sign – Ridgeline Hollow Properties</title>
<link href="https://fonts.googleapis.com/css2?family=Archivo+Black&family=Lexend:wght@400;500&display=swap" rel="stylesheet">
<style>
  :root {
    --stage: #000000;
    --sky-light: #E9F6FB;
    --sky-mid: #45C6F4;
    --brand-blue: #0054A4;
    --brand-mid: #1A7AC4;
    --navy: #14204C;
    --white: #F4FAFD;
  }
  * { margin: 0; padding: 0; box-sizing: border-box; }
  html, body { width: 1200px; height: 755px; overflow: hidden; background: var(--stage); }
  .board { position: relative; width: 1200px; height: 755px; }
  .panel { position: absolute; width: 484px; overflow: hidden; }
  .panel--front { left: 29px; top: 17px; height: 484px; background: var(--sky-light); }
  .panel--back { left: 562px; top: 17px; height: 484px; background: var(--sky-mid); }
  .panel--rider-left { left: 29px; top: 521px; height: 208px; background: var(--sky-light); }
  .panel--rider-right { left: 562px; top: 521px; height: 208px; background: var(--sky-light); }

  .headline {
    font-family: "Archivo Black", sans-serif;
    color: var(--brand-blue);
    letter-spacing: -1px;
  }
  .headline span {
    position: absolute;
    display: block;
    font-size: 112px;
    line-height: 1;
    white-space: nowrap;
  }
  .panel--front .headline span { left: 0; width: 100%; text-align: center; }
  .panel--front .headline .for { top: 73px; padding-right: 16px; }
  .panel--front .headline .sale { top: 170px; }
  .panel--back .headline .for { left: 34px; top: 82px; }
  .panel--back .headline .sale { left: 31px; top: 170px; }

  .mini-brand {
    position: absolute; left: 0; width: 100%; top: 66px;
    text-align: center;
    font-family: "Lexend", sans-serif; font-weight: 500;
    font-size: 15px; color: var(--brand-blue);
  }

  .reach {
    position: absolute; left: 0; width: 100%; top: 308px;
    text-align: center;
    font-family: "Archivo Black", sans-serif;
    font-size: 21px; line-height: 1; color: var(--brand-blue); letter-spacing: -0.3px;
  }

  .phone-band {
    position: absolute; left: 0; top: 338px; width: 100%; height: 106px;
    display: flex; align-items: center; justify-content: center;
    font-family: "Archivo Black", sans-serif; font-size: 55px; letter-spacing: -1px;
  }
  .panel--front .phone-band { background: var(--sky-mid); color: var(--brand-blue); }
  .panel--back .phone-band { background: var(--navy); color: var(--white); }

  .pointer { position: absolute; left: 407px; top: 139px; width: 50px; height: 101px; }

  .rider-brand {
    position: absolute; left: 0; width: 100%; top: 106px; text-align: center;
    font-family: "Lexend", sans-serif; color: var(--brand-mid);
  }
  .rider-brand .name { display: block; font-size: 30px; font-weight: 400; line-height: 1; }
  .rider-brand .tag {
    display: block; margin-top: 8px; font-size: 9px; font-weight: 400;
    letter-spacing: 11px; padding-left: 11px; color: var(--brand-blue);
  }
</style>
</head>
<body>
<main class="board">
  <section class="panel panel--front" aria-label="For sale sign, front">
    <div class="mini-brand">Ridgeline Hollow</div>
    <h1 class="headline"><span class="for">FOR</span><span class="sale">SALE</span></h1>
    <p class="reach">REACH US ON</p>
    <p class="phone-band">(555) 617 3489</p>
  </section>

  <section class="panel panel--back" aria-label="For sale sign, alternate">
    <div class="mini-brand">Ridgeline Hollow</div>
    <h2 class="headline"><span class="for">FOR</span><span class="sale">SALE</span></h2>
    <svg class="pointer" viewBox="0 0 50 101" aria-hidden="true"><polygon points="0,0 50,50.5 0,101" fill="#0054A4"/></svg>
    <p class="reach">REACH US ON</p>
    <p class="phone-band">(555) 617 3489</p>
  </section>

  <section class="panel panel--rider-left" aria-label="Brand rider">
    <div class="rider-brand"><span class="name">Ridgeline Hollow</span><span class="tag">PROPERTIES</span></div>
  </section>

  <section class="panel panel--rider-right" aria-label="Brand rider">
    <div class="rider-brand"><span class="name">Ridgeline Hollow</span><span class="tag">PROPERTIES</span></div>
  </section>
</main>
</body>
</html>
```